Header for Academic Handouts (How-to-Guides)

We are looking for a design element, which can be used as a visual header on A4-word-documents (Portrait-Set-Up). It shall be a graphic, visual language which is clearly understandable. The header height shall be between 0.75 - 1.5 inch – so it should not have too many small details. Attached below ideas/directions how the final document could look like.

The visual element shall symbolize by simple means the topic of “flipped classroom” or “active learning”. The documents with these new graphic elements will be used on handouts which are distributed in this training course:
https://www.kolvabrun.ch/en/the-kolvabrun-hochschule/education/educational-development/didaktische-weiterbildung/flipped-classroom.html

```html
<!DOCTYPE html>
<html lang="en">
<head>
<meta charset="utf-8">
<title>Flipped Classroom – Handout Header</title>
<link href="https://fonts.googleapis.com/css2?family=Arimo:wght@400&display=swap" rel="stylesheet">
<style>
  :root {
    --brand-yellow: #ffcc00;
    --paper: #ffffff;
    --ink: #1c1c1c;
  }
  html, body {
    margin: 0;
    padding: 0;
    width: 927px;
    height: 1200px;
    overflow: hidden;
    background: var(--paper);
  }
  .handout-page {
    position: relative;
    width: 927px;
    height: 1200px;
    background: var(--paper);
  }
  .handout-page svg {
    display: block;
    width: 927px;
    height: 1200px;
  }
  .header-band { fill: var(--brand-yellow); }
  .badge-rim { fill: var(--brand-yellow); }
  .badge-face { fill: var(--paper); }
  .monitor-icon {
    fill: none;
    stroke: var(--ink);
    stroke-width: 3;
    stroke-linejoin: round;
  }
  .monitor-screen { fill: var(--paper); }
  .header-title {
    font-family: "Arimo", Arial, sans-serif;
    font-size: 39px;
    font-weight: 400;
    letter-spacing: 0.5px;
    fill: var(--ink);
  }
  .footer-rule { fill: var(--brand-yellow); }
</style>
</head>
<body>
<main class="handout-page">
  <svg viewBox="0 0 1004 1300" xmlns="http://www.w3.org/2000/svg" aria-labelledby="page-title">
    <!-- header band -->
    <rect class="header-band" x="0" y="0" width="1004" height="111"/>

    <!-- topic badge: diamond with screen icon -->
    <g class="topic-badge">
      <polygon class="badge-rim" points="98,38 171,111 98,185 25,111"/>
      <polygon class="badge-face" points="98,36 168,106 98,176 28,106"/>
      <g class="monitor-icon">
        <rect class="monitor-screen" x="62" y="81" width="74" height="47" rx="3"/>
        <rect x="67" y="86" width="64" height="37" rx="1"/>
        <path d="M93 128 L93 134 M104 128 L104 134"/>
        <rect x="87" y="134" width="23" height="3" rx="1"/>
      </g>
    </g>

    <!-- title -->
    <text id="page-title" class="header-title" x="183" y="83">FLIPPED CLASSROOM</text>

    <!-- footer rule -->
    <rect class="footer-rule" x="0" y="1278" width="1004" height="5"/>
  </svg>
</main>
</body>
</html>
```